Crest Vigor Affiliate Program

We are CrestVigor.com, a growing fitness and wellness community.

As part of our promotional strategy we have a robust Affiliate Program for affiliates to refer customers to us in exchange for a commission payable on each purchase.

We want a highly attractive and enticing short brochure describing the benefits of joining our Affiliate Program. This will be sent to prospective Affiliates to help persuade them to join and promote our products.

Length should be one large landscape page (or two portrait pages opened, magazine style).

I have attached the required text and features that should be included in the design. Particular focus should be placed on the "Why Become a Crest Vigor Affiliate" section and listed reasons.

I have also attached a couple of brochures that I would like to influence the designs I receive. I like the styles and concepts used in these examples.
Updates

Target Market(s)

Males aged 20-35. Amateur and Professional Online Marketers

Industry/Entity Type

Landscape

Requirements
Must have
• Include our Logo (attached).

Very clean, modern use of fonts, text styles and colors.

Must be "web 2.0" style in terms of appearance and graphics to be used.

Absolutely no early 2000s style clipart must be included.
Nice to have
• Cool graphics visually representing the listed reasons "Why Become a Crest Vigor Affiliate"
Should not have
• No clipart.
No cursive fonts.

```html
<!DOCTYPE html>
<html lang="en">
<head>
<meta charset="utf-8">
<title>Crest Vigor Affiliate Program</title>
<link rel="stylesheet" href="https://fonts.googleapis.com/css2?family=Archivo+Black&family=Arvo:wght@700&family=Didact+Gothic&display=swap">
<style>
  :root {
    --page-grey: #c9c9c9;
    --panel-white: #f1f1f1;
    --centre-light: #f3f3f3;
    --centre-dark: #bdbdbd;
    --band-blue: #1a9ad8;
    --deep-blue: #0a5ea6;
    --ribbon-dark: #0b3f78;
    --pale-blue: #dce9f7;
    --heading-blue: #1b9be0;
    --ink: #2d2d2d;
    --logo-ink: #0d2c4f;
    --photo-top: #3b8fd0;
    --photo-mid: #5aa6da;
    --photo-skin: #d7a688;
    --photo-low: #b98a70;
  }
  * { margin: 0; padding: 0; box-sizing: border-box; }
  html, body { width: 1200px; height: 927px; overflow: hidden; background: var(--page-grey); }
  .brochure {
    position: relative; width: 1200px; height: 927px; overflow: hidden;
    background: var(--page-grey);
    font-family: "Didact Gothic", sans-serif; color: var(--ink);
  }
  .panel { position: absolute; top: 0; height: 927px; }
  .panel-left { left: 82px; width: 332px; background: var(--panel-white); }
  .panel-centre { left: 414px; width: 372px; background: radial-gradient(ellipse at 50% 40%, var(--centre-light), var(--centre-dark) 95%); }
  .panel-right { left: 786px; width: 332px; background: var(--panel-white); }
  .band { position: absolute; left: 0; top: 100px; width: 1200px; height: 58px; background: var(--band-blue); }
  .logo-box {
    position: absolute; left: 82px; top: 100px; width: 332px; height: 58px;
    background: var(--pale-blue); display: flex; align-items: center; padding-left: 21px;
  }
  .logo-name { font-family: "Didact Gothic", sans-serif; font-size: 39px; letter-spacing: -1px; color: var(--logo-ink); }
  .ribbon { position: absolute; left: 751px; top: 69px; width: 401px; height: 91px; }
  .ribbon-text {
    position: absolute; left: 751px; top: 77px; width: 401px; text-align: center;
    font-family: "Archivo Black", sans-serif; color: #fff; line-height: 1.1;
  }
  .ribbon-text .lead { display: block; font-size: 14.5px; color: #0c1a2b; }
  .ribbon-text .url { display: block; font-size: 20px; margin-top: 2px; }
  .heading {
    position: absolute; font-family: "Arvo", serif; font-weight: 700;
    font-size: 25px; line-height: 28px; color: var(--heading-blue);
  }
  .heading .strong { color: var(--deep-blue); }
  .body-copy { position: absolute; left: 105px; width: 294px; font-size: 14.6px; line-height: 19.8px; letter-spacing: -0.15px; }
  .photo-area {
    position: absolute; left: 440px; top: 265px; width: 330px; height: 540px;
    border-radius: 46% 46% 30% 30% / 22% 22% 12% 12%;
    background: linear-gradient(180deg, var(--photo-top) 0%, var(--photo-mid) 42%, var(--photo-skin) 58%, var(--photo-low) 100%);
    opacity: 0.85;
  }
  .find-title { position: absolute; left: 105px; top: 684px; font-family: "Arvo", serif; font-weight: 700; font-size: 14.5px; color: var(--heading-blue); }
  .find-title .strong { color: var(--deep-blue); }
  .contact-box {
    position: absolute; left: 69px; top: 709px; width: 358px; height: 119px;
    background: var(--pale-blue); font-style: normal;
    border-left: 13px solid var(--deep-blue); border-right: 13px solid var(--deep-blue);
    font-size: 12px; line-height: 16.6px; letter-spacing: -0.2px;
  }
  .contact-address { position: absolute; left: 22px; top: 7px; width: 140px; }
  .contact-lines { position: absolute; left: 170px; top: 7px; }
  .terms { position: absolute; left: 105px; top: 855px; font-size: 12.4px; }
  .benefits { position: absolute; left: 827px; top: 0; width: 280px; list-style: none; }
  .benefit { position: absolute; left: 0; width: 280px; display: flex; font-size: 14.6px; line-height: 20px; letter-spacing: -0.15px; }
  .tick { flex: none; width: 16px; height: 16px; margin: 2px 11px 0 0; }
</style>
</head>
<body>
<main class="brochure">
  <div class="panel panel-left"></div>
  <div class="panel panel-centre"></div>
  <div class="panel panel-right"></div>
  <div class="band"></div>

  <div class="logo-box"><span class="logo-name">crestvigor.com</span></div>

  <svg class="ribbon" viewBox="0 0 401 91" aria-hidden="true">
    <defs>
      <linearGradient id="ribbonFill" x1="0" y1="0" x2="1" y2="0">
        <stop offset="0" stop-color="#1b7fc4"/>
        <stop offset="0.5" stop-color="#2a9be0"/>
        <stop offset="1" stop-color="#1b7fc4"/>
      </linearGradient>
    </defs>
    <polygon points="0,60 35,60 35,89" fill="var(--ribbon-dark)"/>
    <polygon points="401,60 366,60 366,89" fill="var(--ribbon-dark)"/>
    <rect x="0" y="0" width="401" height="60" fill="url(#ribbonFill)"/>
  </svg>
  <p class="ribbon-text"><span class="lead">Become a Crest Vigor affiliate now at</span><span class="url">CrestPartners.com</span></p>

  <h2 class="heading" style="left:105px;top:227px;">About <span class="strong">Crest Vigor</span></h2>
  <p class="body-copy" style="top:268px;">Crest Vigor is a New York headquartered fitness community. We are open 24/7 at CrestVigor.com<br>Our customers benefit from products that focus on actionable changes and a communi-ty-driven approach to wellness that produce outstanding body transformations.</p>

  <h2 class="heading" style="left:105px;top:435px;">About our<br><span class="strong">Affiliate Program</span></h2>
  <p class="body-copy" style="top:503px;">Second only to how much we love our customers is our commitment to Affiliates. What this means for you as a Crest Vigor affiliate is happy customers, massive social proof and low refund rates. We bend over backwards to help our Affiliates promote, persuade and profit.</p>

  <div class="photo-area" role="img" aria-label="Photo of a woman in a blue hoodie and shorts stretching her arms out wide"></div>

  <h3 class="find-title">Where to <span class="strong">Find Us</span></h3>
  <address class="contact-box">
    <p class="contact-address">Crest Vigor<br>42 Harbor St, Suite 9B<br>Brookline&nbsp;&nbsp;10284<br>United States</p>
    <p class="contact-lines">Phone:<br>555 012 3478<br>Email:<br>partners@crestvigor.com<br>Web:<br>CrestPartners.com</p>
  </address>
  <p class="terms">Full terms and conditions at CrestPartners.com</p>

  <h2 class="heading" style="left:806px;top:227px;">Why Become a<br><span class="strong">Crest Vigor Affiliate</span></h2>

  <svg width="0" height="0" style="position:absolute" aria-hidden="true">
    <symbol id="tick" viewBox="0 0 16 16">
      <rect x="0.5" y="0.5" width="15" height="15" rx="2" fill="#2d8fd6"/>
      <rect x="3" y="3" width="10" height="10" fill="#fff"/>
      <path d="M4.5 8.2 L7 10.6 L11.6 5" fill="none" stroke="#0c1a2b" stroke-width="1.8"/>
    </symbol>
  </svg>

  <ul class="benefits">
    <li class="benefit" style="top:297px;"><svg class="tick"><use href="#tick"/></svg><span>customer endorses tried-<br>and-tested products</span></li>
    <li class="benefit" style="top:345px;"><svg class="tick"><use href="#tick"/></svg><span>expertly crafted persuasive copy</span></li>
    <li class="benefit" style="top:374px;"><svg class="tick"><use href="#tick"/></svg><span>continual conversion<br>optimization</span></li>
    <li class="benefit" style="top:422px;"><svg class="tick"><use href="#tick"/></svg><span>75% plus commission rates</span></li>
    <li class="benefit" style="top:451px;"><svg class="tick"><use href="#tick"/></svg><span>bonus commission rates<br>for top affiliates</span></li>
    <li class="benefit" style="top:499px;"><svg class="tick"><use href="#tick"/></svg><span>lifetime commissions on all<br>eligible customer purchases</span></li>
    <li class="benefit" style="top:548px;"><svg class="tick"><use href="#tick"/></svg><span>regular affiliate contests<br>and high value prizes</span></li>
    <li class="benefit" style="top:596px;"><svg class="tick"><use href="#tick"/></svg><span>unprecedented affiliate<br>training site</span></li>
    <li class="benefit" style="top:645px;"><svg class="tick"><use href="#tick"/></svg><span>ready to go promotional tools</span></li>
    <li class="benefit" style="top:674px;"><svg class="tick"><use href="#tick"/></svg><span>cut and paste ready promotions</span></li>
    <li class="benefit" style="top:702px;"><svg class="tick"><use href="#tick"/></svg><span>bespoke marketing tools<br>for JV partners</span></li>
    <li class="benefit" style="top:751px;"><svg class="tick"><use href="#tick"/></svg><span>dedicated affiliate support</span></li>
  </ul>
</main>
</body>
</html>
```